Web design for business website

I need a web design for a business website for one of our clients who is specialized in alarm management software. I would like you to design 3 web pages, one for each of the 3 pages. You need to process the corporate identity of our client to the web design. This means the colors of the logo (red and black) should definitely show up on all of the 3 pages. Find the logo file for the logo of our customer. To increase readability I suggest you use a white/light background. All suggestions are welcome.

Target Market(s)

B2B, Alarm management

Industry/Entity Type

Business

Number of Pages Required

3 page

Requirements
Must have
• The web design must have exactly the same structure as the wireframes and needs to contain the colors of the company logo.

```html
<!DOCTYPE html>
<html lang="en">
<head>
<meta charset="utf-8">
<title>Verital – Industry</title>
<link href="https://fonts.googleapis.com/css2?family=Lato:wght@300;400;700;900&display=swap" rel="stylesheet">
<style>
:root{
  --navy:#1d1b3b;
  --orange:#e8461e;
  --page:#efefef;
  --white:#ffffff;
  --text:#555555;
  --muted:#9a9a9a;
  --line:#cfcfcf;
  --btn:#ececec;
}
*{box-sizing:border-box;margin:0;padding:0}
html,body{width:1200px;height:1100px;overflow:hidden}
body{font-family:"Lato",sans-serif;background:var(--white);color:var(--text);font-size:12px}
.wrap{width:648px;margin-left:270px;position:relative}
/* top bar */
.topbar{height:27px;border-bottom:1px solid #e4e4e4}
.topbar .wrap{display:flex;align-items:center;height:27px;justify-content:space-between}
.phone{font-size:10px;color:#222}
.top-tools{display:flex;gap:6px}
.lang{width:56px;height:22px;border:1px solid var(--line);display:flex;align-items:center;font-size:10px;font-weight:700;color:#222;padding-left:8px;position:relative}
.lang::after{content:"";position:absolute;right:0;top:0;width:18px;height:20px;border-left:1px solid var(--line)}
.lang svg{position:absolute;right:5px;top:8px}
.search{width:126px;height:22px;border:1px solid var(--line);font-size:9px;color:var(--muted);padding:5px 7px}
/* header */
.header{height:68px;border-bottom:1px solid #e4e4e4}
.header .wrap{display:flex;align-items:center;justify-content:space-between;height:68px}
.brand{display:flex;align-items:center;gap:9px}
.brand-mark{width:14px;height:14px;background:var(--orange)}
.brand-name{font-size:24px;font-weight:700;letter-spacing:1px;color:var(--navy);line-height:1}
.brand-tag{font-size:8px;color:var(--text);margin-top:3px}
.actions{display:flex;gap:6px}
.actions a{width:74px;height:27px;display:flex;align-items:center;justify-content:center;font-size:9px;color:#555;background:var(--btn);border:1px solid var(--line);text-decoration:none}
.actions a.signup{background:var(--orange);color:var(--white);border-color:var(--orange)}
/* nav */
.nav{height:28px}
.nav .wrap{display:flex;height:28px;align-items:center}
.nav a{font-size:10px;color:#444;text-decoration:none;margin-right:38px}
.nav a.active{color:var(--orange)}
/* main */
.main{background:var(--page);height:515px}
.main .wrap{display:flex;justify-content:space-between;height:515px}
.content{width:462px;padding-top:33px}
.content p{font-size:8.6px;line-height:14.3px;color:#555;margin-bottom:16px}
.form-card{background:var(--white);height:227px;margin-top:10px;padding:18px 22px}
.form-card h2{font-size:11px;font-weight:400;color:#666;margin-bottom:13px}
.form-grid{display:grid;grid-template-columns:198px 198px;column-gap:20px;row-gap:9px}
.field{height:27px;border:1px solid var(--line);font-size:8px;color:var(--muted);padding:8px 7px}
.field.tall{height:83px}
.send{align-self:end;height:27px;background:var(--navy);color:var(--white);font-size:9px;display:flex;align-items:center;justify-content:center;margin-bottom:2px}
.sidebar{width:175px;display:flex;flex-direction:column}
.ad{height:172px;border-bottom:1px solid var(--line)}
.ad-idea{background:radial-gradient(circle at 50% 40%,#5a6478,#2c3344)}
.ad-camp{background:linear-gradient(160deg,#f2f2f2,#bdbdbd 60%,#4b4b4b)}
.ad-web{background:linear-gradient(135deg,#ffffff 40%,#5cc0e8 60%,#ffffff 80%);border:1px solid var(--line)}
/* clients */
.clients{background:var(--navy);height:174px;padding-top:32px}
.clients h2{text-align:center;color:var(--white);font-size:21px;font-weight:700;letter-spacing:.5px}
.clients h2 span{font-weight:300}
.rule{width:106px;margin:8px auto 0;border-top:1px solid #8b8aa3;border-bottom:1px solid #8b8aa3;height:3px}
.client-row{background:var(--white);height:59px;margin-top:15px;display:flex;align-items:center;justify-content:center;gap:40px}
.client{display:flex;align-items:center;gap:6px;font-size:14px;font-weight:700;color:#7c7c7c}
.client i{display:block;width:13px;height:13px;border-radius:50%;background:#9c9c9c}
/* social strip */
.social{height:35px}
.social .wrap{display:flex;align-items:center;justify-content:space-between;height:35px}
.networks{display:flex;gap:22px}
.networks span{font-size:13px;font-weight:900}
.n1{color:var(--navy)}.n2,.n3{color:var(--orange)}
.subscribe{display:flex}
.subscribe .email{width:186px;height:22px;border:1px solid var(--orange);font-size:8px;color:var(--orange);padding:6px 6px}
.subscribe .go{width:82px;height:22px;background:var(--orange);color:var(--white);font-size:8.5px;display:flex;align-items:center;justify-content:center}
/* footer */
.footer{background:var(--page);height:209px}
.footer .wrap{display:flex;height:209px}
.cols{display:flex;padding-top:19px;width:472px}
.col{width:118px}
.col h3{font-size:11px;font-weight:700;color:#333;margin-right:10px;padding-bottom:6px;border-bottom:3px double #bbbbbb;margin-bottom:12px}
.col a{display:block;font-size:8.5px;color:#444;text-decoration:none;margin-bottom:8px}
.col a.current{color:var(--orange);text-decoration:underline}
.contact{width:176px;background:var(--navy);color:var(--white);padding:20px 24px;font-size:8.3px;line-height:14px}
.contact .brand-mark{width:11px;height:11px;background:#e6e6e6}
.contact .brand-name{font-size:17px;color:#e6e6e6}
.contact .brand-tag{font-size:6.5px;color:#ccc;margin-top:2px}
.contact .brand{margin-bottom:14px}
.contact p{margin-bottom:10px}
.contact p.second{margin-top:18px}
.ci{display:flex;align-items:center;gap:8px;margin-bottom:10px}
.ci b{width:20px;height:20px;border:1px solid #fff;border-radius:50%;display:flex;align-items:center;justify-content:center}
.copyright{height:44px;border-top:1px solid #e4e4e4;text-align:center;font-size:8px;color:#777;padding-top:17px}
</style>
</head>
<body>
<div class="topbar"><div class="wrap">
  <span class="phone">T +31 (0) 20 5550 184</span>
  <div class="top-tools">
    <div class="lang">ENG<svg width="7" height="4"><path d="M0 0h7L3.5 4z" fill="#999"/></svg></div>
    <div class="search">Search</div>
  </div>
</div></div>

<div class="header"><div class="wrap">
  <div class="brand"><span class="brand-mark"></span><div><div class="brand-name">VERITAL</div><div class="brand-tag">Live alarm intelligence</div></div></div>
  <div class="actions"><a href="#">ACCOUNT</a><a href="#">LOGIN</a><a class="signup" href="#">SIGN UP</a></div>
</div></div>

<nav class="nav"><div class="wrap">
  <a href="#">Home</a><a class="active" href="#">Industry</a><a href="#">Telecom</a><a href="#">Power</a><a href="#">Utilities</a><a href="#">Infra</a><a href="#">Store</a>
</div></nav>

<main class="main"><div class="wrap">
  <section class="content">
    <p>Dynamisch engagement van bedrijfsmeta-services voor door de markt gestimuleerde gegevens. Samenwerkend herstel van gebruikers over verschillende platforms vóór op klant gerichte vervaardigde producten. Overtuigende ontwikkeling van verticale portalen op lange termijn met hoge impact via visionaire oplossingen. Professionele aanwending van gestandaardiseerde portalen ten opzichte van te leveren producten die de bronnen maximaliseren.<br>Dynamische optimalisatie volledig onderzochte resultaten voor onafhankelijk menselijke kapitaal. Complete overheersing van naadloze synergie via interoperabele methodologieën.</p>
    <p>Dynamisch engagement van bedrijfsmeta-services voor door de markt gestimuleerde gegevens. Samenwerkend herstel van gebruikers over verschillende platforms vóór op klant gerichte vervaardigde producten. Overtuigende ontwikkeling van verticale portalen op lange termijn met hoge impact via visionaire oplossingen.</p>
    <p>Dynamisch engagement van bedrijfsmeta-services voor door de markt gestimuleerde gegevens. Samenwerkend herstel van gebruikers over verschillende platforms vóór op klant gerichte vervaardigde producten. Overtuigende ontwikkeling van verticale portalen op lange termijn met hoge impact via visionaire oplossingen.</p>
    <div class="form-card">
      <h2>For more information about a particular service :</h2>
      <div class="form-grid">
        <div class="field">Name</div><div class="field">Email</div>
        <div class="field">Telephone</div><div></div>
        <div class="field tall">Comments</div><div class="send">SEND REQUEST</div>
      </div>
    </div>
  </section>
  <aside class="sidebar">
    <div class="ad ad-idea" role="img" aria-label="Banner: light bulb illustration with play button, Submit an idea"></div>
    <div class="ad ad-camp" role="img" aria-label="Banner: video bootcamp advert with camera lens photo, register today"></div>
    <div class="ad ad-web" role="img" aria-label="Banner: website design offer starting from 35 dollars with pencils illustration"></div>
  </aside>
</div></main>

<section class="clients">
  <h2>CLIENTS <span>Using...</span></h2>
  <div class="rule"></div>
  <div class="wrap client-row">
    <span class="client"><i></i>Norvex</span>
    <span class="client"><i></i>Kelvra</span>
    <span class="client">Brouwstad</span>
    <span class="client">polymerfield</span>
    <span class="client"><i></i>TARVIK FUEL</span>
  </div>
</section>

<div class="social"><div class="wrap">
  <div class="networks"><span class="n1">Chirpline</span><span class="n2">ClipCast</span><span class="n3">WorkNet</span></div>
  <div class="subscribe"><div class="email">Enter Your Email Address</div><div class="go">SUBSCRIBE</div></div>
</div></div>

<footer class="footer"><div class="wrap">
  <div class="cols">
    <div class="col"><h3>Solutions</h3><a href="#">Signal Reporting</a><a class="current" href="#">Signal Insight</a><a href="#">Signal Advisor</a><a href="#">CORE</a></div>
    <div class="col"><h3>Industries</h3><a href="#">Industry</a><a href="#">Telcom</a><a href="#">Power</a><a href="#">Utilities</a><a href="#">Infra</a></div>
    <div class="col"><h3>About Us</h3><a href="#">Company</a><a href="#">Overview</a><a href="#">Leadership</a><a href="#">Partners</a><a href="#">Location</a></div>
    <div class="col"><h3>News</h3><a href="#">Product News</a><a href="#">Partner News</a><a href="#">Events</a><a href="#">Press Releases</a><a href="#">Vacancies</a></div>
  </div>
  <div class="contact">
    <div class="brand"><span class="brand-mark"></span><div><div class="brand-name">VERITAL</div><div class="brand-tag">Live alarm intelligence</div></div></div>
    <p>#123, Street Name, City Name<br>Country CH - 1234</p>
    <div class="ci"><b><svg width="10" height="10" viewBox="0 0 10 10"><path d="M2 1l2 2-1 1.3a6 6 0 0 0 2.7 2.7L7 6l2 2-1.2 1.2C4.5 9 1 5.5.8 2.2z" fill="#fff"/></svg></b>(44) 555 010 2288</div>
    <div class="ci"><b><svg width="10" height="8" viewBox="0 0 10 8"><rect x=".5" y=".5" width="9" height="7" fill="none" stroke="#fff"/><path d="M.5.5l4.5 4 4.5-4" fill="none" stroke="#fff"/></svg></b>info@example.com</div>
    <p class="second">#123, Street Name, City Name<br>Country CH - 1234</p>
  </div>
</div></footer>

<div class="copyright">Copyright 2015 VERITAL. All Rights Reserved.</div>
</body>
</html>
```